A New and modern Business Card for Tarvish Commerce Partners Ltd

New and modern Logo and Business Card Attached is the current logo/business card designCurrently the business is called "Tarvish & Co." or TCP Ltd for short. This is subject to change.This business specialises in Telecoms and Energy. We work with the major networks (QX, Z7, etc) and also offer Energy Products saving clients money off their energy bills.These are business to business services.The current design incorporates a Pheonix, indicating rebirth, starting something new.We would like to maintain the Phoenix element but a newer modern style.We love colours in the logo 3 max.The aim of this is to be ultra slick and modern. I envisage Tarvish & Co. on one side of the card with long descriptions on the other side.Side 1:TCP Ltd/Logo?Side 2:TCP Ltd/Logo/Graphic?Brogan & Co.Name:Address:Phone:Email:The design is mostly flexible but must incorporate a Phoenix.For example "Tarvish & Co." with a block phoenix behind the text...up to you.

Industry/Entity Type

Telecommunications

Contact Information for Business Card

Tarvish & Co.
Address:
Name:
Phone:
Email:

Logo Text

Tarvish & Co.

Colors
33a6d7
0792cd
acd037
9bcb3c
f78f20
fece3e

Requirements
Must have
• Phoenix
• 3/4 colours max
• Blue representing Technology (wireless)
• Green for Eco Energy
• Orange for Phoenix
• White business card background
Should not have
• phoenix must not all be red/ orange fire, we are a technology service company and the phoenix colours must represent this. Fire is not representative of our company.

```html
<!DOCTYPE html>
<html lang="en">
<head>
<meta charset="utf-8">
<title>Tarvish Commerce Partners Ltd – Business Card</title>
<link rel="stylesheet" href="https://fonts.googleapis.com/css2?family=Lato:wght@400;700&family=Cinzel:wght@600&display=swap">
<style>
  :root {
    --page: #ffffff;
    --card-front: #ffffff;
    --card-back: #3a3a3a;
    --ink: #2b2b2b;
    --ink-soft: #6a6a6a;
    --tech-blue: #0792cd;
    --tech-blue-light: #33a6d7;
    --eco-green: #9bcb3c;
    --phoenix-orange: #f78f20;
    --accent-faint: #e3f1d0;
    --on-dark: #ffffff;
  }
  * { margin: 0; padding: 0; box-sizing: border-box; }
  html, body {
    width: 996px; height: 1200px; overflow: hidden;
    background: var(--page);
  }
  .canvas { position: relative; width: 996px; height: 1200px; }

  .card {
    position: absolute; left: 108px; width: 840px; height: 489px;
    overflow: hidden;
  }
  .card--front { top: 70px; background: var(--card-front); }
  .card--back  { top: 621px; background: var(--card-back); }

  /* front */
  .brand-mark {
    position: absolute; left: 620px; top: 70px; width: 170px;
    display: flex; flex-direction: column; align-items: center; gap: 12px;
  }
  .brand-mark__dot {
    width: 84px; height: 84px; border-radius: 50%;
    background: linear-gradient(135deg, var(--tech-blue-light), var(--tech-blue));
  }
  .brand-mark__name {
    font-family: "Lato", sans-serif; font-weight: 700; font-size: 20px;
    letter-spacing: 2px; color: var(--phoenix-orange);
  }
  .corner-accent {
    position: absolute; left: 700px; top: 270px;
    width: 260px; height: 240px; border-radius: 50%;
    background: var(--accent-faint);
  }

  .person { position: absolute; left: 94px; top: 192px; }
  .person__name {
    font-family: "Lato", sans-serif; font-weight: 700; font-size: 31px;
    color: var(--ink); letter-spacing: 0.5px; line-height: 1;
  }
  .person__role {
    margin-top: 6px;
    font-family: "Lato", sans-serif; font-weight: 400; font-size: 14px;
    color: var(--ink-soft); letter-spacing: 0.3px;
  }

  .contact-list {
    position: absolute; left: 97px; top: 305px; list-style: none;
  }
  .contact-list__item {
    display: flex; align-items: center; gap: 14px;
    height: 31px;
    font-family: "Lato", sans-serif; font-size: 19px; color: var(--ink);
    letter-spacing: 0.4px;
  }
  .contact-list__icon { width: 17px; height: 17px; flex: none; fill: var(--tech-blue); }

  .eco-band {
    position: absolute; left: 0; bottom: 0; width: 100%; height: 8px;
    background: linear-gradient(90deg, var(--tech-blue), var(--eco-green));
  }

  /* back */
  .back-mark {
    position: absolute; left: 0; right: 0; top: 96px;
    display: flex; flex-direction: column; align-items: center;
  }
  .back-mark__dot {
    width: 170px; height: 170px; border-radius: 50%;
    background: var(--phoenix-orange);
  }
  .back-mark__name {
    margin-top: 58px;
    font-family: "Cinzel", serif; font-weight: 600; font-size: 50px;
    color: var(--on-dark); letter-spacing: 2px; line-height: 1;
  }
  .back-band {
    position: absolute; left: 0; bottom: 0; width: 100%; height: 8px;
    background: linear-gradient(90deg, var(--tech-blue), var(--eco-green));
  }
</style>
</head>
<body>
<main class="canvas">

  <section class="card card--front" aria-label="Card front">
    <div class="corner-accent"></div>
    <div class="brand-mark">
      <span class="brand-mark__dot"></span>
      <span class="brand-mark__name">TCP LTD</span>
    </div>

    <div class="person">
      <h1 class="person__name">YOUR NAME</h1>
      <p class="person__role">YOUR DESIGNATION</p>
    </div>

    <ul class="contact-list">
      <li class="contact-list__item">
        <svg class="contact-list__icon" viewBox="0 0 24 24" aria-hidden="true"><path d="M6.6 10.8a15.1 15.1 0 0 0 6.6 6.6l2.2-2.2a1 1 0 0 1 1-.25 11.4 11.4 0 0 0 3.6.57 1 1 0 0 1 1 1V20a1 1 0 0 1-1 1A17 17 0 0 1 3 4a1 1 0 0 1 1-1h3.5a1 1 0 0 1 1 1c0 1.25.2 2.45.57 3.57a1 1 0 0 1-.25 1z"/></svg>
        <span>120.555.0148</span>
      </li>
      <li class="contact-list__item">
        <svg class="contact-list__icon" viewBox="0 0 24 24" aria-hidden="true"><path d="M2 5h20v14H2z"/><path d="M3 6l9 6.3L21 6" fill="none" stroke="#fff" stroke-width="1.6"/></svg>
        <span>mail@tarvish.com</span>
      </li>
      <li class="contact-list__item">
        <svg class="contact-list__icon" viewBox="0 0 24 24" aria-hidden="true"><circle cx="12" cy="12" r="10"/><path d="M2 12h20M12 2c3 3 3 17 0 20M12 2c-3 3-3 17 0 20" fill="none" stroke="#fff" stroke-width="1.4"/></svg>
        <span>www.tarvish.com</span>
      </li>
      <li class="contact-list__item">
        <svg class="contact-list__icon" viewBox="0 0 24 24" aria-hidden="true"><path d="M12 2a7 7 0 0 0-7 7c0 5.2 7 13 7 13s7-7.8 7-13a7 7 0 0 0-7-7zm0 9.5A2.5 2.5 0 1 1 12 6.5a2.5 2.5 0 0 1 0 5z"/></svg>
        <span>47, Marlow Lane, Hollybrook, London</span>
      </li>
    </ul>
    <div class="eco-band"></div>
  </section>

  <section class="card card--back" aria-label="Card back">
    <div class="back-mark">
      <span class="back-mark__dot"></span>
      <span class="back-mark__name">TCP LTD</span>
    </div>
    <div class="back-band"></div>
  </section>

</main>
</body>
</html>
```